small business website design

***Update: need the design to be coded into a wordpress or similar format***
Need a website for a small business with big plans. No online ordering etc but business description and contact details pages, a page showing products we use and page for customers or suppliers to register with us. Also want links to quillane. We have a logo existing but also open to any improvements on the design. We have an existing website we created and looks very DIY but you can get some info from it to help create your design for us.
Updates
Hi Everyone, we didn't make it clear at the beginning but we would like the final design to be in a coded format and ready to upload to a URL. I have to apologise and admit to my lack of knowledge of the design process.
Target Market(s)
Oil / gas and industrial plant managers.
Industry/Entity Type
Small Business
Look and feel
Each slider illustrates characteristics of the customer's brand and the style your logo design should communicate.

```html
<!DOCTYPE html>
<html lang="en">
<head>
<meta charset="utf-8">
<title>Harbourline Level Services</title>
<link rel="stylesheet" href="https://fonts.googleapis.com/css2?family=Cabin:wght@400;500;600&family=Open+Sans:wght@400;600;700&display=swap">
<style>
:root{
  --blue:#2a95cf;
  --blue-light:#45b3e6;
  --blue-dark:#1f7fb3;
  --nav-active:#2b86bd;
  --text:#555;
  --text-dark:#333;
  --border:#d6d6d6;
  --panel:#f0f0f0;
  --footer-top:#3a3e44;
  --footer-bottom:#17191c;
  --white:#fff;
}
*{box-sizing:border-box;margin:0;padding:0}
html,body{width:769px;height:1200px;overflow:hidden;background:var(--white)}
body{position:relative;font-family:"Open Sans",Arial,sans-serif;color:var(--text)}
.abs{position:absolute}

/* header */
.brand-mark{left:55px;top:24px;width:84px;height:84px;background:#9aa0a6;border-radius:6px}
.brand-name{left:155px;top:34px;font-family:"Cabin",sans-serif;font-size:23px;line-height:30px;color:var(--text-dark)}
.phone{left:500px;top:42px;width:214px;display:flex;justify-content:flex-end;align-items:center;gap:8px;font-family:"Cabin",sans-serif;font-size:17px;color:var(--blue)}
.search{left:546px;top:80px;width:167px;height:23px;border:1px solid var(--border);font-size:9px;color:#777;padding:5px 6px}
.search svg{position:absolute;right:6px;top:6px}

/* nav */
.nav{left:0;top:126px;width:769px;height:37px;background:linear-gradient(#4fb8e8,#2c9ad3)}
.nav a{position:absolute;top:0;height:37px;line-height:37px;text-align:center;color:var(--white);font-size:11px;font-weight:700;text-decoration:none;text-transform:uppercase;border-right:1px solid rgba(0,0,0,.1)}
.nav a.active{background:var(--nav-active)}

/* hero */
.hero{left:0;top:163px;width:769px;height:276px;background:linear-gradient(#a9b8c9 0%,#d9dde2 25%,#e8e8e6 55%,#7a6a55 62%,#b8b2a8 75%,#6f6a62 100%)}
.hero-arrow{position:absolute;top:120px;width:30px;height:30px;border-radius:50%;background:rgba(120,120,120,.55)}
.hero-caption{position:absolute;top:183px;width:100%;text-align:center;font-family:"Cabin",sans-serif;font-size:23px;color:var(--white)}

/* main */
.heading{font-family:"Cabin",sans-serif;font-size:18px;color:var(--blue);font-weight:400}
.intro-photo{left:56px;top:523px;width:158px;height:105px;background:linear-gradient(#b9c7d6,#8e9a8a 60%,#6b6f72)}
.body-text{font-size:10px;line-height:16.5px;color:var(--text)}
.intro-text{left:234px;top:519px;width:208px;font-size:9px;line-height:15.5px;word-break:break-all}
.intro-more{left:55px;top:648px;width:390px;font-size:9.5px;line-height:16px}
.news-item{left:58px;top:720px;width:375px;padding-left:17px}
.news-item::before{content:"";position:absolute;left:1px;top:5px;width:7px;height:7px;border:1px solid #777;border-radius:50%;background:radial-gradient(#555 40%,transparent 45%)}
.more{left:380px;top:773px;width:49px;text-align:right;font-size:10px;color:var(--blue)}
.product{position:absolute;top:832px;width:119px}
.product-img{height:92px;border:1px solid var(--border);display:flex;align-items:center;justify-content:center}
.product-img span{display:block;width:50px;height:62px;border-radius:8px}
.product p{font-size:10px;text-align:center;margin-top:5px;color:var(--text)}

/* side */
.register{left:498px;top:487px;width:216px;height:300px;background:var(--panel);border:1px solid #e2e2e2}
.register h2{position:absolute;top:15px;width:100%;text-align:center;font-family:Arial,sans-serif;font-size:17px;font-weight:400;color:var(--blue-dark)}
.field{position:absolute;left:11px;width:194px;height:27px;background:var(--white);border:1px solid #ccc;font-size:9px;color:#666;padding:7px 9px}
.submit{position:absolute;left:35px;top:255px;width:153px;height:31px;background:var(--blue);border-bottom:3px solid #1b6f9e;color:var(--white);font-size:12px;text-align:center;line-height:29px;border-radius:2px}
.follow{left:498px;top:814px;width:216px;height:125px;border:1px solid #e2e2e2;background:#fbfbfb}
.follow h2{position:absolute;left:13px;top:12px;font-family:"Cabin",sans-serif;font-size:18px;font-weight:400;color:var(--blue)}
.follow p{position:absolute;left:13px;top:43px;width:195px;font-size:9.5px;line-height:16px;color:var(--text)}
.social{position:absolute;top:86px;width:24px;height:24px}

/* footer */
.footer{left:0;top:982px;width:769px;height:172px;background:linear-gradient(var(--footer-top),#202327)}
.footer-bar{left:0;top:1154px;width:769px;height:46px;background:var(--footer-bottom);border-top:1px solid #2c2f33}
.footer-col{position:absolute;top:36px;color:var(--white)}
.footer-col h3{font-size:10.5px;font-weight:700;margin-bottom:8px}
.footer-col li{list-style:none;font-size:9.5px;line-height:18.5px}
.newsletter{position:absolute;left:539px;top:28px;width:174px;color:var(--white)}
.newsletter h3{font-family:Arial,sans-serif;font-size:14px;font-weight:400;margin-bottom:6px}
.newsletter p{font-size:9.5px;line-height:18.5px}
.newsletter .email{margin-top:6px;height:22px;background:var(--white);border:1px solid #aaa}
.newsletter .subscribe{margin:12px 0 0 95px;width:79px;height:23px;background:var(--blue);font-size:10.5px;line-height:23px;text-align:center}
.copyright{position:absolute;left:56px;top:15px;font-size:9.5px;color:var(--white)}
</style>
</head>
<body>

<header>
  <div class="abs brand-mark" aria-hidden="true"></div>
  <div class="abs brand-name">Harbourline Level<br>Services</div>
  <div class="abs phone">+61 (0)7 5550 0123
    <svg width="16" height="20" viewBox="0 0 16 20" aria-hidden="true"><path d="M3 1c1-1 2 0 3 2l1 3c0 1-1 2-2 2 0 3 2 6 4 7 1-1 2-1 3 0l2 2c1 1 0 2-1 3-5 2-12-8-10-19z" fill="#2a95cf"/></svg>
  </div>
  <div class="abs search">Search..
    <svg width="10" height="10" viewBox="0 0 10 10" aria-hidden="true"><circle cx="4" cy="4" r="3" fill="none" stroke="#999" stroke-width="1.3"/><path d="M6.2 6.2 9 9" stroke="#999" stroke-width="1.4"/></svg>
  </div>
</header>

<nav class="abs nav">
  <a class="active" style="left:55px;width:73px">Home</a>
  <a style="left:128px;width:80px">About Us</a>
  <a style="left:208px;width:93px">Services</a>
  <a style="left:301px;width:91px">Products</a>
  <a style="left:392px;width:121px">News &amp; Events</a>
  <a style="left:513px;width:108px">Testimonials</a>
  <a style="left:621px;width:93px">Contact</a>
</nav>

<section class="abs hero" role="img" aria-label="Photograph of white fuel storage tanks at a waterfront terminal">
  <span class="hero-arrow" style="left:53px"><svg width="30" height="30" viewBox="0 0 30 30" aria-hidden="true"><path d="M17 9l-6 6 6 6" fill="none" stroke="#fff" stroke-width="1.5"/></svg></span>
  <span class="hero-arrow" style="left:684px"><svg width="30" height="30" viewBox="0 0 30 30" aria-hidden="true"><path d="M13 9l6 6-6 6" fill="none" stroke="#fff" stroke-width="1.5"/></svg></span>
  <p class="hero-caption">Providing instrumentation expertise for your plant</p>
</section>

<main>
  <h1 class="abs heading" style="left:55px;top:483px">Welcome to Harbourline Level Services</h1>
  <div class="abs intro-photo" role="img" aria-label="Photograph of two technicians in hi-vis gear on a tank roof"></div>
  <p class="abs body-text intro-text">We provide instrumentation expertise for the liquid storage industry in Australia and Papua New Guinea. From initial design concept through installation, routine maintenance and calibration of various systems, brands and technologies. Talk to us about your requirements and we will tailor a solution to meet your needs.</p>
  <p class="abs body-text intro-more">Whether it be ongoing service support of your existing assets, or helping you to find the right technology from major vendors to fit your latest project.</p>

  <h2 class="abs heading" style="left:55px;top:688px">Latest News</h2>
  <p class="abs body-text news-item">Supplier lead times letting you down? We're now carrying stock of common instrumentation from various vendors&nbsp; - so when the chips are down we can get your plant back on its feet. Talk to us about your needs?</p>
  <span class="abs more">More..</span>

  <h2 class="abs heading" style="left:55px;top:800px">Products</h2>
  <div class="product" style="left:55px">
    <div class="product-img" role="img" aria-label="Product photo of a radar tank level gauge"><span style="background:linear-gradient(#6f8ca8,#c9ced3)"></span></div>
    <p>Vantor Tank Gauging</p>
  </div>
  <div class="product" style="left:183px">
    <div class="product-img" role="img" aria-label="Product photo of a tank display unit"><span style="background:linear-gradient(#4d8fc0,#2c6e9e)"></span></div>
    <p>Vantor Tank Gauging</p>
  </div>
  <div class="product" style="left:311px">
    <div class="product-img" role="img" aria-label="Product photo of a level probe transmitter"><span style="background:linear-gradient(#5a8ed0,#9aa4ae)"></span></div>
    <p>Vantor Tank Gauging</p>
  </div>
</main>

<aside>
  <form class="abs register">
    <h2>Register With Us</h2>
    <div class="field" style="top:50px">Name</div>
    <div class="field" style="top:89px">Phone</div>
    <div class="field" style="top:128px">E-mail</div>
    <div class="field" style="top:167px;height:72px">Message</div>
    <div class="submit">Submit Request</div>
  </form>
  <div class="abs follow">
    <h2>Follow us</h2>
    <p>Follow us on the social network and get our latest updates</p>
    <span class="social" style="left:13px;background:#3b5998" aria-label="quillane"></span>
    <span class="social" style="left:45px;background:#2a9fd6" aria-label="Short posts"></span>
    <span class="social" style="left:76px;background:#f07a1f" aria-label="Feed"></span>
    <span class="social" style="left:108px;background:#d6312b" aria-label="Video"></span>
    <span class="social" style="left:139px;background:#7a5240" aria-label="Photos"></span>
  </div>
</aside>

<footer>
  <div class="abs footer">
    <div class="footer-col" style="left:56px">
      <h3>Maintenance</h3>
      <ul><li>Planned Maintenance</li><li>System calibrations</li><li>validations and verification</li><li>System monitoring</li><li>Emergency Breakdowns</li></ul>
    </div>
    <div class="footer-col" style="left:228px">
      <h3>Project Support</h3>
      <ul><li>Project Management</li><li>Accurate Level Gauging</li><li>Reporting systems</li><li>System commissioning</li><li>Operational Training</li></ul>
    </div>
    <div class="footer-col" style="left:392px">
      <h3>Company</h3>
      <ul><li>About</li><li>Testimonials</li><li>Affiliate Program</li><li>Privacy Policy</li><li>Terms of Service</li></ul>
    </div>
    <div class="newsletter">
      <h3>Newsletter</h3>
      <p>Stay in touch with us by signing up for our quarterly newsletter!</p>
      <div class="email"></div>
      <div class="subscribe">SUBSCRIBE</div>
    </div>
  </div>
  <div class="abs footer-bar"><p class="copyright">Copyright ©2013. All Rights Reserved.</p></div>
</footer>

</body>
</html>
```